1 Dimensional cover for digital product

Please note that if a designer comes in with an original design and other designers try to copy them too closely I will always work with the original designer in order to get the actual look I want.
Therefore it is in the interests of the designers to get their concepts in first.

I am designing some audio products for football (soccer players).

I would like a square version and a 16:9 version of the packaging completed. The square version will be for the Valmbo audio cover and the 16:9 for the thumbnails of videos.

I would like the final images in PSP files as a template that I can change the title and the main image.

I am open to creativity in this project but would like it to be a luxury and premium in what it is portraying.

I have added my logo and also the packaging that I currently use on my sister website which is not aimed at football, soccer.

I've also included an image of one of my models. This would NOT be the product image, but it could be a background image, or you may choose to leave it out altogether.

I've also included an example image as the main product image.

Although I have chosen greyscale I would also like to see products with colour.

The product page is at https://brevalink.shop/collections/all
I add this so that you can chose any one of the titles for this template

Target Market(s)

This is aimed at professional footballers

Industry/Entity Type

Sporting Good

Font styles to use
Serif
Sans Serif

Colors

Designer to choose colors to be used in the design.

Requirements
Must have
• This must look like it is made for an affluent market.
• It may also be simple in its design but I do not wish to be too prescriptive with creativity.
• My typography is Montserrat
Nice to have
• Can include the colors of my logos:
• #5BA9DE
• #272B5F
• Or you can choose to go with greyscale
Should not have
• This is a product for serious athletes so it should look very professional and adult orientated (so not cartoonish its look)

```html
<!DOCTYPE html>
<html lang="en">
<head>
<meta charset="utf-8">
<title>After Game – Hypnosis Sessions Cover</title>
<link rel="stylesheet" href="https://fonts.googleapis.com/css2?family=Montserrat:wght@400;500;600&display=swap">
<style>
  :root {
    --gold: #b2a57a;
    --gold-deep: #a39666;
    --sky: #5ba9de;
    --white: #ffffff;
    --smoke-light: #b9b09a;
    --smoke-mid: #6e6a5c;
    --smoke-dark: #1c1c1a;
    --ink: #0d0d0d;
  }
  html, body {
    margin: 0;
    padding: 0;
    width: 1200px;
    height: 1200px;
    overflow: hidden;
    background: var(--ink);
  }
  .cover {
    position: relative;
    width: 1200px;
    height: 1200px;
    overflow: hidden;
    font-family: "Montserrat", sans-serif;
  }
  .cover__art {
    position: absolute;
    inset: 0;
  }
  .brand {
    position: absolute;
    left: 40px;
    top: 78px;
    width: 410px;
    text-align: center;
    color: var(--white);
  }
  .brand__dot {
    display: block;
    width: 46px;
    height: 46px;
    margin: 0 auto 16px;
    border-radius: 50%;
    background: var(--white);
  }
  .brand__name {
    margin: 0;
    font-size: 17px;
    font-weight: 600;
    letter-spacing: 0.04em;
    text-transform: uppercase;
  }
  .kicker {
    position: absolute;
    left: 137px;
    top: 584px;
    margin: 0;
    font-size: 32px;
    font-weight: 500;
    color: var(--gold);
  }
  .title {
    position: absolute;
    left: 0;
    top: 630px;
    width: 1200px;
    margin: 0;
    font-weight: 600;
    font-size: 214px;
    line-height: 186px;
    letter-spacing: -0.01em;
    color: var(--sky);
  }
  .title__line { display: block; }
  .title__line--after { padding-left: 198px; }
  .title__line--game { padding-left: 290px; }
  .tagline {
    position: absolute;
    left: 118px;
    top: 1076px;
    display: flex;
    align-items: center;
    gap: 50px;
  }
  .tagline__diamond {
    width: 36px;
    height: 36px;
    background: var(--gold);
    transform: rotate(45deg);
    flex: none;
  }
  .tagline__text {
    margin: 0;
    font-size: 25px;
    font-weight: 400;
    line-height: 36px;
    letter-spacing: 0.02em;
    color: var(--sky);
    text-transform: uppercase;
  }
</style>
</head>
<body>
<main class="cover">
  <svg class="cover__art" width="1200" height="1200" viewBox="0 0 1200 1200">
    <defs>
      <radialGradient id="smoke" cx="0.78" cy="0.32" r="0.85">
        <stop offset="0" stop-color="var(--smoke-light)"/>
        <stop offset="0.45" stop-color="var(--smoke-mid)"/>
        <stop offset="1" stop-color="var(--smoke-dark)"/>
      </radialGradient>
      <linearGradient id="shade" x1="0" y1="0" x2="0.6" y2="1">
        <stop offset="0" stop-color="#3a3a36"/>
        <stop offset="1" stop-color="#0e0e0d"/>
      </linearGradient>
    </defs>
    <rect class="photo-main" width="1200" height="1200" fill="url(#smoke)"
          role="img" aria-label="Footballer leaping to head a ball against a smoky golden sky"/>
    <polygon class="photo-shade" points="0,40 0,1200 1200,1200" fill="url(#shade)" opacity="0.82"
             role="img" aria-label="Faded second player striking a ball in a darker diagonal band"/>
    <polygon class="brand-triangle" points="0,0 540,0 245,350 0,62" fill="var(--gold)"/>
  </svg>

  <div class="brand">
    <span class="brand__dot"></span>
    <p class="brand__name">Hale Corwin Hypnotherapy</p>
  </div>

  <p class="kicker">Hypnosis sessions</p>

  <h1 class="title">
    <span class="title__line title__line--after">AFTER</span>
    <span class="title__line title__line--game">GAME</span>
  </h1>

  <div class="tagline">
    <span class="tagline__diamond"></span>
    <p class="tagline__text">Conditioning you towards<br>even better future performances.</p>
  </div>
</main>
</body>
</html>
```